Business Card Design Project

i need a bussines car design
Veltra Clinical Hypnotherapy

Gordon Wexley
Psychotherapy & Hypnosis

64029381 /0427956120

back of the card appoinment space.

file was provided on a PDF, LOgo , use the blu colorsa as well , elegant, clear,

Target Market(s)

young professional, caucasian , young mothers.

Industry/Entity Type

Business

```html
<!DOCTYPE html>
<html lang="en">
<head>
<meta charset="utf-8">
<title>Veltra Clinical Hypnotherapy – Business Card</title>
<link href="https://fonts.googleapis.com/css2?family=Open+Sans:wght@400;600;700&display=swap" rel="stylesheet">
<style>
  :root {
    --bg: #e8e5e2;
    --card: #ffffff;
    --blue: #0a72ba;
    --blue-dark: #075c98;
    --cyan: #1c9ad6;
    --grey: #7a7a7a;
    --grey-light: #a9a9a9;
    --text: #555555;
    --photo-a: #e9d8c4;
    --photo-b: #c9b29a;
  }
  * { box-sizing: border-box; margin: 0; padding: 0; }
  html, body { width: 1200px; height: 789px; overflow: hidden; }
  body {
    background: var(--bg);
    font-family: "Open Sans", Arial, sans-serif;
    color: var(--text);
    position: relative;
  }
  .card {
    position: absolute;
    top: 230px;
    width: 540px;
    height: 330px;
    background: var(--card);
    border-radius: 18px;
    overflow: hidden;
    box-shadow: 0 6px 20px rgba(0,0,0,.18);
  }
  .card--back { left: 45px; }
  .card--front { left: 615px; }

  /* Back */
  .back-header { text-align: center; padding-top: 26px; line-height: 1.35; }
  .back-title { color: var(--blue); font-weight: 700; font-size: 16px; }
  .back-line { font-size: 13px; color: var(--text); }
  .back-email { font-size: 11.5px; font-weight: 700; color: #444; }
  .appointments-title {
    text-align: center; color: var(--blue); font-weight: 700;
    font-size: 14px; margin-top: 12px;
  }
  .appointments {
    display: grid; grid-template-columns: 1fr 1fr;
    row-gap: 16px; column-gap: 14px;
    padding: 16px 26px 0; font-size: 12.5px; color: var(--text);
    white-space: nowrap;
  }
  .back-note {
    text-align: center; font-size: 9.5px; color: var(--grey);
    margin-top: 22px; line-height: 1.35; padding: 0 40px;
  }
  .registration {
    text-align: center; color: var(--blue); font-weight: 700;
    font-size: 12.5px; margin-top: 6px;
  }

  /* Front */
  .photo {
    position: absolute; left: 392px; top: 18px; width: 132px; height: 240px;
    background: linear-gradient(180deg, var(--photo-a), var(--photo-b));
    border-radius: 6px;
  }
  .front-art { position: absolute; inset: 0; }
  .brand {
    position: absolute; left: 36px; top: 72px;
    display: flex; align-items: center; gap: 10px;
  }
  .brand-mark {
    width: 30px; height: 30px; border-radius: 50%; background: var(--blue);
  }
  .brand-name { font-size: 23px; font-weight: 400; color: var(--blue); letter-spacing: .2px; }
  .brand-web {
    position: absolute; left: 76px; top: 108px;
    font-size: 10px; color: #444; letter-spacing: .6px;
    border-top: 1.5px solid var(--blue); padding-top: 2px;
  }
  .person { position: absolute; left: 40px; top: 162px; }
  .person-name { color: var(--cyan); font-size: 15.5px; }
  .person-role { color: var(--grey); font-size: 13px; }
  .contact {
    position: absolute; right: 24px; bottom: 18px; text-align: right;
    color: #fff; line-height: 1.55;
  }
  .contact-phone { font-size: 13px; display: flex; align-items: center; justify-content: flex-end; gap: 6px; }
  .contact-web { font-size: 14.5px; }
</style>
</head>
<body>

  <section class="card card--back" aria-label="Card back">
    <div class="back-header">
      <p class="back-title">VELTRA Clinical Hypnotherapy</p>
      <p class="back-line">By Appointment. Phone: 0427 956 120</p>
      <p class="back-line">148 Hollis Street, Brenwick 3027</p>
      <p class="back-email">reception@veltraclinicalhypnotherapy.com.au</p>
    </div>
    <p class="appointments-title">Your Appointments</p>
    <div class="appointments">
      <span>1.____am/pm ____________ __/__/__</span>
      <span>2.____am/pm ____________ __/__/__</span>
      <span>3.____am/pm ____________ __/__/__</span>
      <span>4.____am/pm ____________ __/__/__</span>
      <span>5.____am/pm ____________ __/__/__</span>
      <span>6.____am/pm ____________ __/__/__</span>
    </div>
    <p class="back-note">To reschedule your appointment, please SMS or phone<br>0427 956 120 at least 24 hours prior to your allocated time. Thank you.</p>
    <p class="registration">NHRA Registration No. 20517</p>
  </section>

  <section class="card card--front" aria-label="Card front">
    <div class="photo" role="img" aria-label="Portrait photograph of Gordon Wexley"></div>
    <svg class="front-art" viewBox="0 0 540 330" width="540" height="330" aria-hidden="true">
      <path d="M0 238 C120 262 260 212 380 176 C450 156 510 150 540 150 L540 172 C470 172 400 196 330 222 C220 262 110 280 0 262 Z" fill="var(--grey-light)"/>
      <path d="M0 262 C110 284 230 262 340 220 C420 190 490 172 540 170 L540 330 L0 330 Z" fill="var(--blue)"/>
      <path d="M0 262 C110 284 230 262 340 220 C420 190 490 172 540 170" fill="none" stroke="#ffffff" stroke-width="3"/>
    </svg>
    <div class="brand">
      <span class="brand-mark"></span>
      <span class="brand-name">Veltra Hypnotherapy</span>
    </div>
    <p class="brand-web">www.veltraclinicalhypnotherapy.com.au</p>
    <div class="person">
      <p class="person-name">Gordon Wexley</p>
      <p class="person-role">Psychotherapy &amp; Hypnosis</p>
    </div>
    <div class="contact">
      <p class="contact-phone">
        <svg width="13" height="13" viewBox="0 0 24 24" aria-hidden="true"><path fill="#fff" d="M6.6 10.8a15.1 15.1 0 0 0 6.6 6.6l2.2-2.2a1 1 0 0 1 1-.25 11.4 11.4 0 0 0 3.6.57 1 1 0 0 1 1 1V20a1 1 0 0 1-1 1A17 17 0 0 1 3 4a1 1 0 0 1 1-1h3.5a1 1 0 0 1 1 1c0 1.25.2 2.45.57 3.57a1 1 0 0 1-.25 1z"/></svg>
        64029381 /0427956120
      </p>
      <p class="contact-web">www.veltraclinicalhypnotherapy.com.au</p>
    </div>
  </section>

</body>
</html>
```